BoltCrewBoard Postcard Campaign

We need a postcard design for our company, BoltCrewBoard.com - we are a job board for mechanics and auto technicians. We are sending a postcard to 1000 auto shops and trucking companies across the US to try to get them to come to our website and purchase a job pack and post a job posting. We will be offering them a promotion of "Save $20 on your first job post. Enter 'SUMMER20' at checkout."

We would like to see designs that are consistent with our website theme. The final design should communicate:
- Access to a targeted and local audience of only auto and truck mechanics and technicians
- Search 50,000 resumes
- Money back guarantee

Target Market(s)

Auto mechanic shops, car dealerships looking for mechanics, truck fleet management looking for technicians

Industry/Entity Type

It Company

Font styles to use
Sans Serif

Colors
0392cd
ec1f27
1b1b1b
cbcbcb
ffffff
3277b5

Requirements
Must have
• See content/copy upload
• - Match website color scheme and look and feel
Should not have
• No photos that look like stock photos - preferably steer away from photos unless it looks great

```html
<!DOCTYPE html>
<html lang="en">
<head>
<meta charset="utf-8">
<title>BoltCrewBoard Postcard</title>
<link href="https://fonts.googleapis.com/css2?family=Oswald:wght@500;600;700&family=Roboto+Condensed:wght@300;400;700&family=Roboto:wght@900&display=swap" rel="stylesheet">
<style>
  :root {
    --backdrop: #7f7e82;
    --white: #ffffff;
    --ink: #333333;
    --red: #ec1f27;
    --blue: #2a6db5;
    --blue-text: #2a6db5;
    --footer: #333333;
  }
  * { margin: 0; padding: 0; box-sizing: border-box; }
  html, body { width: 1200px; height: 975px; overflow: hidden; }
  body { background: var(--backdrop); position: relative; font-family: "Roboto Condensed", sans-serif; }

  .postcard { position: absolute; left: 80px; top: 86px; width: 1040px; height: 802px; background: var(--white); }

  .header { position: absolute; left: 0; top: 0; width: 1040px; height: 254px; }
  .brand-dot { position: absolute; left: 31px; top: 51px; width: 170px; height: 170px; border-radius: 50%; background: var(--ink); }
  .headline { position: absolute; left: 222px; top: 34px; font-family: "Oswald", sans-serif; font-weight: 700; font-size: 106px; line-height: 84px; color: var(--ink); letter-spacing: 0.5px; text-transform: uppercase; }
  .headline span { display: block; white-space: nowrap; }
  .headline .accent { color: var(--red); }

  .features { position: absolute; left: 0; top: 254px; width: 1040px; height: 285px; background: var(--blue); }
  .feature { position: absolute; top: 20px; width: 320px; text-align: center; color: var(--white); }
  .feature svg { display: block; margin: 0 auto; }
  .feature p { font-weight: 300; font-size: 24px; line-height: 29px; margin-top: 12px; }
  .feature.post { left: 28px; }
  .feature.reach { left: 368px; }
  .feature.resumes { left: 725px; }
  .feature.post p { margin-top: 10px; }
  .feature.resumes p { margin-top: 20px; }

  .contact { position: absolute; left: 0; top: 539px; width: 1040px; height: 160px; }
  .site-name { position: absolute; left: 215px; top: 34px; font-family: "Oswald", sans-serif; font-weight: 600; font-size: 50px; line-height: 60px; color: var(--ink); text-transform: uppercase; white-space: nowrap; }
  .phone { position: absolute; left: 285px; top: 101px; font-family: "Roboto", sans-serif; font-weight: 900; font-size: 28px; letter-spacing: 1.5px; color: var(--blue-text); white-space: nowrap; }
  .contact-dot { position: absolute; left: 743px; top: 26px; width: 108px; height: 108px; border-radius: 50%; background: var(--ink); }

  .footer { position: absolute; left: 0; top: 699px; width: 1040px; height: 103px; background: var(--footer); color: var(--white); text-align: center; font-weight: 700; font-size: 29px; line-height: 34px; padding-top: 17px; }
</style>
</head>
<body>
  <main class="postcard">
    <header class="header">
      <div class="brand-dot" aria-hidden="true"></div>
      <h1 class="headline">
        <span>Find Your Next</span>
        <span><span class="accent" style="display:inline">Mechanic</span> Today</span>
      </h1>
    </header>

    <section class="features">
      <div class="feature post">
        <svg width="120" height="112" viewBox="0 0 120 112" aria-hidden="true">
          <g transform="rotate(14 60 62)">
            <rect x="20" y="24" width="88" height="78" fill="none" stroke="#fff" stroke-width="5"/>
            <text x="64" y="78" text-anchor="middle" font-family="Oswald, sans-serif" font-weight="700" font-size="24" fill="#fff">JOBS</text>
          </g>
          <circle cx="30" cy="20" r="14" fill="#fff"/>
          <line x1="36" y1="28" x2="54" y2="48" stroke="#fff" stroke-width="5" stroke-linecap="round"/>
        </svg>
        <p>Post a job with us and get access to hundreds of qualified technicians in your area</p>
      </div>

      <div class="feature reach">
        <svg width="142" height="112" viewBox="0 0 142 112" aria-hidden="true">
          <rect x="6" y="6" width="124" height="80" rx="4" fill="none" stroke="#fff" stroke-width="6"/>
          <rect x="58" y="86" width="20" height="12" fill="#fff"/>
          <rect x="42" y="98" width="52" height="6" fill="#fff"/>
          <circle cx="104" cy="74" r="20" fill="var(--blue)" stroke="#fff" stroke-width="6"/>
          <line x1="118" y1="88" x2="134" y2="104" stroke="#fff" stroke-width="8" stroke-linecap="round"/>
        </svg>
        <p>Includes distribution and promotion across multiple job boards, such as HireLane.com, TalentDock and WorkReach.com</p>
      </div>

      <div class="feature resumes">
        <svg width="112" height="116" viewBox="0 0 112 116" aria-hidden="true">
          <path d="M8 4 H68 L90 26 V108 H8 Z" fill="none" stroke="#fff" stroke-width="6" stroke-linejoin="round"/>
          <text x="47" y="46" text-anchor="middle" font-family="Oswald, sans-serif" font-weight="600" font-size="17" fill="#fff">Resume</text>
          <rect x="20" y="60" width="52" height="5" fill="#fff"/>
          <rect x="20" y="74" width="40" height="5" fill="#fff"/>
          <rect x="20" y="88" width="44" height="5" fill="#fff"/>
          <circle cx="86" cy="92" r="20" fill="#fff"/>
          <rect x="76" y="89" width="20" height="6" fill="var(--blue)"/>
          <rect x="83" y="82" width="6" height="20" fill="var(--blue)"/>
        </svg>
        <p>Search 50,000+ resumes, with new candidates added daily</p>
      </div>
    </section>

    <section class="contact">
      <div class="site-name">BoltCrewBoard.com</div>
      <div class="phone">CALL: (800) 555-0142</div>
      <div class="contact-dot" aria-hidden="true"></div>
    </section>

    <footer class="footer">
      Connecting automotive employers with qualified technicians since 2006<br>
      100% satisfaction guaranteed, or your money back
    </footer>
  </main>
</body>
</html>
```